Packiging of mouse trap

We need a packiging for a new mousetrap called 'Quillnest'. It is a mouse/rat trap. We want to have it pretty simple and modern. The logo of the mouse trap is in the attachment and the measures of the packaging also (don't look at the design, it has nothing to do with us). It's needs to stand out in between the other packaging due to it's simplicity and modern touch.

Font styles to use
Sans Serif

Requirements
Must have
• Simplicity, modern
Should not have
• Too many colors

```html
<!DOCTYPE html>
<html lang="en">
<head>
<meta charset="utf-8">
<title>Quillnest Electric Mouse Trap – Packaging</title>
<link href="https://fonts.googleapis.com/css2?family=Montserrat:wght@500;600;800&family=Michroma&display=swap" rel="stylesheet">
<style>
  :root{
    --bg:#dcdcdc;
    --ink-dark:#1e1f20;
    --paper:#ffffff;
    --paper-soft:#f1f1f1;
    --logo-grey:#c9c9c9;
    --green:#6cbf4a;
    --text-light:#f4f4f4;
    --text-dark:#3a3a3a;
    --rule:#bdbdbd;
  }
  *{margin:0;padding:0;box-sizing:border-box}
  html,body{width:1200px;height:960px;overflow:hidden;background:var(--bg)}
  .canvas{position:relative;width:1200px;height:960px;background:radial-gradient(circle at 45% 45%,#f0f0f0,#cfcfcf 90%)}
  .dieline{position:absolute;left:300px;top:90px;display:flex;height:780px;box-shadow:0 20px 40px rgba(0,0,0,.18)}
  .panel{position:relative;height:100%;display:flex;flex-direction:column;overflow:hidden}
  .panel--side{width:200px}
  .panel--front{width:400px}
  .panel__top{position:relative;height:480px}
  .panel__bottom{position:relative;flex:1;display:flex;flex-direction:column;align-items:center;padding-top:58px}
  .panel--side .panel__top{background:linear-gradient(160deg,#2a2b2c,#161718)}
  .panel--side .panel__bottom{background:linear-gradient(180deg,#f4f4f4,#e4e4e4);color:var(--text-dark);padding-top:46px}
  .panel--front .panel__top{background:linear-gradient(170deg,var(--paper),var(--paper-soft))}
  .panel--front .panel__bottom{background:var(--ink-dark);color:var(--text-light)}
  .pattern{position:absolute;inset:0}
  .ribbon{position:absolute;top:24px;width:78px;height:82px;background:var(--green);color:#fff;
    clip-path:polygon(0 0,100% 0,100% 100%,50% 86%,0 100%);
    font-family:"Montserrat",sans-serif;font-weight:600;font-size:10px;line-height:1.25;text-align:center;padding-top:10px}
  .panel--front .ribbon{left:36px;width:78px;font-size:10.5px}
  .panel--side .ribbon{left:12px;width:30px;height:90px;font-size:6px;padding-top:8px}
  .ribbon hr{border:0;border-top:1px solid rgba(255,255,255,.8);margin:4px 8px}
  .brand{position:absolute;font-family:"Montserrat",sans-serif;font-weight:800;white-space:nowrap;line-height:1;
    writing-mode:vertical-rl;transform:translate(-50%,-50%) rotate(180deg)}
  .panel--front .brand{color:var(--logo-grey);font-size:56px;left:60%;top:290px;letter-spacing:1px}
  .panel--side .brand{color:var(--text-light);font-size:34px;left:58%;top:330px}
  .title{font-family:"Michroma",sans-serif;text-align:center;line-height:1.75;font-weight:400}
  .panel--front .title{font-size:19px}
  .panel--side .title{font-size:11px}
  .features{list-style:none;display:grid;grid-template-columns:1fr 1fr;margin-top:26px;font-family:"Montserrat",sans-serif;font-weight:500}
  .panel--front .features{font-size:11px;width:300px}
  .panel--side .features{font-size:7px;width:156px;margin-top:18px}
  .feature{display:flex;align-items:center;gap:7px;padding:8px 10px;white-space:nowrap}
  .panel--side .feature{gap:4px;padding:7px 5px}
  .feature:nth-child(odd){border-right:1px solid var(--rule)}
  .feature:nth-child(-n+2){border-bottom:1px solid var(--rule)}
  .feature svg{flex:none}
  .panel--front .feature svg{width:20px;height:20px}
  .panel--side .feature svg{width:12px;height:12px}
  .site{font-family:"Montserrat",sans-serif;font-weight:500;letter-spacing:.5px;margin-top:auto;margin-bottom:46px}
  .panel--front .site{font-size:9.5px}
  .panel--side .site{font-size:6.5px}
</style>
</head>
<body>
<div class="canvas">
  <div class="dieline">

    <section class="panel panel--side">
      <div class="panel__top">
        <div class="pattern" role="img" aria-label="Faint circuit-line and mouse pattern on dark grey"></div>
        <div class="ribbon">INSTANT KILL TRAP<hr>PET SAFE</div>
        <div class="brand">Quillnest</div>
      </div>
      <div class="panel__bottom">
        <h2 class="title">ELECTRIC<br>MOUSE TRAP</h2>
        <ul class="features">
          <li class="feature"><svg viewBox="0 0 20 20"><circle cx="10" cy="10" r="8.5" fill="none" stroke="currentColor"/><path d="M6 10l3 3 5-6" fill="none" stroke="currentColor"/></svg>Easy to use</li>
          <li class="feature"><svg viewBox="0 0 20 20"><circle cx="10" cy="10" r="8.5" fill="none" stroke="currentColor"/><path d="M6 9a4 4 0 0 1 7-2M14 11a4 4 0 0 1-7 2" fill="none" stroke="currentColor"/></svg>Reusable</li>
          <li class="feature"><svg viewBox="0 0 20 20"><circle cx="10" cy="10" r="8.5" fill="none" stroke="currentColor"/><path d="M6 8h8M6 12h8" stroke="currentColor"/></svg>No Injuries</li>
          <li class="feature"><svg viewBox="0 0 20 20"><circle cx="10" cy="10" r="8.5" fill="none" stroke="currentColor"/><path d="M11 4l-4 7h4l-2 5" fill="none" stroke="currentColor"/></svg>Powerful</li>
        </ul>
        <p class="site">WWW.QUILLNEST-HOME.COM</p>
      </div>
    </section>

    <section class="panel panel--front">
      <div class="panel__top">
        <div class="pattern" role="img" aria-label="Faint light-grey circuit-line and mouse pattern on white"></div>
        <div class="ribbon">INSTANT<br>KILL TRAP<hr>PET SAFE</div>
        <div class="brand">Quillnest</div>
      </div>
      <div class="panel__bottom">
        <h1 class="title">ELECTRIC<br>MOUSE TRAP</h1>
        <ul class="features">
          <li class="feature"><svg viewBox="0 0 20 20"><circle cx="10" cy="10" r="8.5" fill="none" stroke="currentColor"/><path d="M6 10l3 3 5-6" fill="none" stroke="currentColor"/></svg>Easy to use</li>
          <li class="feature"><svg viewBox="0 0 20 20"><circle cx="10" cy="10" r="8.5" fill="none" stroke="currentColor"/><path d="M6 9a4 4 0 0 1 7-2M14 11a4 4 0 0 1-7 2" fill="none" stroke="currentColor"/></svg>Reusable</li>
          <li class="feature"><svg viewBox="0 0 20 20"><circle cx="10" cy="10" r="8.5" fill="none" stroke="currentColor"/><path d="M6 8h8M6 12h8" stroke="currentColor"/></svg>No Injuries</li>
          <li class="feature"><svg viewBox="0 0 20 20"><circle cx="10" cy="10" r="8.5" fill="none" stroke="currentColor"/><path d="M11 4l-4 7h4l-2 5" fill="none" stroke="currentColor"/></svg>Powerful</li>
        </ul>
        <p class="site">WWW.QUILLNEST-HOME.COM</p>
      </div>
    </section>

  </div>
</div>
</body>
</html>
```